Business Card, Stationery, Folder and Notepad Design
I need double sided standard sized Business Card [3.5" x 2"]
up to designer
Professional
Wes Harlan
27400 W. Pelham Rd.
Pine Hollow
IL
415-932-7104 ext 582
wessy@quillmarkdeeds.example
I don't want to see just the business card designs. Please submit a design for all four things mentioned otherwise it will be eliminated.
Order Now at www.quillmarkdeeds.example

```html
<!DOCTYPE html>
<html lang="en">
<head>
<meta charset="utf-8">
<title>Quillmark Deeds Stationery Set</title>
<link href="https://fonts.googleapis.com/css2?family=Cormorant+Garamond:wght@600&family=Open+Sans:wght@400&display=swap" rel="stylesheet">
<style>
:root{
  --board:#2b2b2b;
  --paper:#fbfbfb;
  --ink:#3a3a3a;
  --orange:#e07a1c;
  --orange-soft:#f3b36b;
  --dark:#1f1f1f;
  --shadow:rgba(0,0,0,.5);
}
*{margin:0;padding:0;box-sizing:border-box}
html,body{width:1200px;height:262px;overflow:hidden;background:var(--board)}
.board{position:relative;width:1200px;height:262px;background:radial-gradient(ellipse at 50% 40%,#353535,var(--board))}
.item{position:absolute;background:var(--paper);box-shadow:0 2px 6px var(--shadow);overflow:hidden}
.brand{display:flex;align-items:center;gap:3px;font-family:"Cormorant Garamond",serif;font-weight:600;color:var(--ink);text-transform:uppercase;white-space:nowrap}
.brand .mark{display:block;background:var(--orange)}
.glow{position:absolute;left:0;right:0;bottom:0;background:linear-gradient(to right,var(--dark) 0%,#6a3a10 35%,var(--orange) 50%,#6a3a10 65%,var(--dark) 100%)}
.watermark{position:absolute;background:var(--orange-soft);opacity:.18}
.fine{font-family:"Open Sans",sans-serif;color:#777;line-height:1.3}
/* business cards */
.card{width:77px;height:36px}
.card .brand{position:absolute;left:6px;top:6px;font-size:4px}
.card .brand .mark{width:5px;height:5px}
.card .fine{position:absolute;left:6px;top:16px;font-size:2.6px}
.card-back{background:var(--dark)}
.card-back .brand{color:var(--paper);left:22px;top:15px;font-size:4.5px}
/* letterheads */
.letter{width:154px;height:204px}
.letter .brand{position:absolute;left:14px;top:12px;font-size:5px}
.letter .brand .mark{width:6px;height:6px}
.letter .watermark{left:60px;top:70px;width:40px;height:40px}
.letter .glow{height:16px}
.letter .fine{position:absolute;left:14px;bottom:4px;font-size:2.6px;color:#ddd}
/* compliment slips and envelopes */
.slip{width:125px;height:76px}
.slip .brand{position:absolute;left:8px;top:8px;font-size:4px}
.slip .brand .mark{width:5px;height:5px}
.slip .glow{height:8px}
.env-dark{background:var(--dark)}
.env-dark .flap{position:absolute;left:0;right:0;top:0;height:30px;background:linear-gradient(#5a3310,var(--orange) 60%,var(--dark))}
.env-dark .mark{position:absolute;left:56px;top:10px;width:10px;height:10px;background:var(--paper)}
.env-light .band{position:absolute;left:0;right:0;top:0;height:22px;background:var(--dark)}
.env-light .band span{position:absolute;left:57px;top:8px;width:8px;height:8px;background:var(--orange)}
/* folder */
.folder{left:754px;top:24px;width:432px;height:206px;display:flex}
.folder .panel{position:relative;flex:1;border-right:1px solid #ddd}
.folder .panel:last-child{border:none}
.folder .watermark{left:70px;top:60px;width:60px;height:60px}
.folder .glow{height:14px}
.folder .brand{position:absolute;left:26px;top:52px;font-size:14px;gap:6px}
.folder .brand .mark{width:18px;height:18px}
.folder .tagline{position:absolute;left:50px;top:72px;font-size:4px}
</style>
</head>
<body>
<main class="board">
  <!-- business cards -->
  <div class="item card" style="left:19px;top:98px">
    <div class="brand"><span class="mark"></span>Quillmark Deeds</div>
    <p class="fine">Wes Harlan<br>415-932-7104 ext 582<br>wessy@quillmarkdeeds.example</p>
  </div>
  <div class="item card" style="left:19px;top:140px">
    <div class="brand"><span class="mark"></span>Quillmark Deeds</div>
    <p class="fine">27400 W. Pelham Rd.<br>Pine Hollow, IL<br>www.quillmarkdeeds.example</p>
  </div>
  <div class="item card card-back" style="left:19px;top:182px">
    <div class="brand">Quillmark Deeds</div>
  </div>

  <!-- letterheads -->
  <div class="item letter" style="left:134px;top:24px">
    <div class="brand"><span class="mark"></span>Quillmark Deeds</div>
    <div class="watermark"></div>
    <div class="glow"></div>
    <p class="fine">27400 W. Pelham Rd. Pine Hollow IL · 415-932-7104 · www.quillmarkdeeds.example</p>
  </div>
  <div class="item letter" style="left:307px;top:24px">
    <div class="watermark"></div>
    <div class="glow"></div>
  </div>

  <!-- slips -->
  <div class="item slip" style="left:470px;top:38px">
    <div class="brand"><span class="mark"></span>Quillmark Deeds</div>
    <div class="glow"></div>
  </div>
  <div class="item slip" style="left:470px;top:130px">
    <div class="brand"><span class="mark"></span>Quillmark Deeds</div>
    <div class="glow" style="height:20px"></div>
  </div>

  <!-- envelopes -->
  <div class="item slip env-dark" style="left:610px;top:38px">
    <div class="flap"></div><span class="mark"></span>
  </div>
  <div class="item slip env-light" style="left:610px;top:130px">
    <div class="band"><span></span></div>
  </div>

  <!-- folder -->
  <div class="item folder">
    <div class="panel">
      <div class="watermark"></div>
      <div class="glow"></div>
    </div>
    <div class="panel">
      <div class="brand"><span class="mark"></span>Quillmark Deeds</div>
      <p class="fine tagline">Trusted title and escrow service</p>
      <div class="glow"></div>
    </div>
  </div>
</main>
</body>
</html>
```